QUORVIX - Sydney Based Technology Consultancy -Logo & Business Card design

Who are we?
-
Quorvix is an emerging and advanced technology consulting and professional services business based in Sydney, Australia. Quorvix specialising in increasing value to organisations through the effective use of current and emerging technologies, ensuring that technology is a sustainable catalyst to attaining stated business goals.

We pride ourselves in challenging the norm.

What do we want?
-
We are looking to update our "Brand" we already have a simple “home grown” logo and we are now looking for a new one, once we have this updated logo and businesses look and feel though the business card design we will refresh our website with the new logo and design thus updating the Companies overall look at feel.

Our current site is www.quorvix-example.net.au is a very basic wordpress site and we will be updating it once we have the new logo and designs done

Our initial thoughts on the new Quorvix identity are
• Logo Concept
- One of the key things is obviously the 8
- I was thinking that a logo that had 8 as the core of the logo would be cool,
- Almost like having a “ring” or hoop that is twisted to form an 8 with different services scribed on the inside.
- So we would have a Large 8 and the inside would have ring each service or section engraved.

• Brand / web Feel
- Simple
- Professional
- Innovative
- Clear
- Destination
- Unique
- Impartial
- Safe
- Leading edge
- Familiar

- Emerging technologies
- White and ice / glacier blue
- The familiar feel of the Brindle web site
- Embedded specialist Video clips

• Portfolio of Services
- Quorvix – A smart place for Smart people
- Quorvix – we provide the process to take ideas from awareness to reality
- Focus should be on the brand quality consistent clear local knowledge with regional, national, theatre and global presence

Access to Specialists
- Emerging technologies
- Sustainability
- Collaboration
- Data centre
- Virtualisation

• Adjacent ideas under the one Brand
- Tembrosk – Enable Business Collaboration
- Plinsk – Infrastructure Virtualisation
- morvo - smart people and processes
- skandel - Emerging technologies
- brunhavel - business to technology integration
- tolpin - Smart Infrastructure
- yusk – Connected communities
- dwol - sustainability

Target Market(s)

Australia, New Zealand and Asia pacific organisations that are typically English speaking.
Markets
- IT & Technology partners
- Banking and Finance
- Health

Industry/Entity Type

Business

Requirements
Must have
• Logo
Business cards
Colour pallette
3D Logo
Nice to have
• Style guide
Designer who can also assist with new Wordpress design
Should not have
• we don't want cheap looking, overtly flashy or gimmicky logo.

```html
<!DOCTYPE html>
<html lang="en">
<head>
<meta charset="utf-8">
<title>Quorvix – Business Card</title>
<link rel="stylesheet" href="https://fonts.googleapis.com/css2?family=Source+Sans+3:ital,wght@0,400;0,600;0,700;1,400&display=swap">
<style>
  :root {
    --backdrop: #b9b9b9;
    --card-ice: #f4f8fa;
    --card-back: #43547a;
    --slate: #3f5078;
    --navy: #1d3a78;
    --ink-navy: #1c3675;
    --logo-blue: #4d5f8c;
    --gold: #e3b93a;
    --logo-gold: #d9c25a;
    --mint: #cfe0d9;
    --white: #ffffff;
  }
  * { box-sizing: border-box; margin: 0; padding: 0; }
  html, body {
    width: 1200px;
    height: 900px;
    overflow: hidden;
  }
  body {
    background: var(--backdrop);
    font-family: "Source Sans 3", "Myriad Pro", sans-serif;
    display: flex;
    align-items: center;
    justify-content: center;
    gap: 40px;
  }
  .card {
    width: 540px;
    height: 310px;
    position: relative;
    overflow: hidden;
    box-shadow: 0 6px 18px rgba(0,0,0,0.25);
  }

  /* Back of card */
  .card-back {
    background: var(--card-back);
    display: flex;
    align-items: center;
    justify-content: center;
  }
  .card-back .brand-name {
    color: var(--logo-gold);
    font-size: 64px;
    font-weight: 600;
    letter-spacing: 1px;
  }

  /* Front of card */
  .card-front {
    background: var(--card-ice);
  }
  .identity {
    position: absolute;
    top: 0;
    left: 0;
    right: 0;
    height: 210px;
    display: flex;
    flex-direction: column;
    align-items: center;
    justify-content: center;
    padding-top: 6px;
  }
  .identity .brand-name {
    color: var(--logo-blue);
    font-size: 70px;
    font-weight: 700;
    line-height: 1;
  }
  .identity .person-name {
    color: var(--ink-navy);
    font-size: 36px;
    font-weight: 400;
    line-height: 1.1;
    margin-top: 4px;
  }
  .contact-row {
    position: absolute;
    top: 210px;
    left: 0;
    right: 0;
    height: 40px;
    display: grid;
    grid-template-columns: 1fr 1fr 1fr;
  }
  .contact-cell {
    display: flex;
    align-items: center;
    justify-content: center;
    font-size: 12px;
    color: var(--white);
    padding: 0 8px;
    white-space: nowrap;
  }
  .contact-address { background: var(--slate); font-style: italic; justify-content: flex-start; }
  .contact-email { background: var(--gold); }
  .contact-phone { background: var(--mint); }
  .web-band {
    position: absolute;
    top: 250px;
    left: 0;
    right: 0;
    bottom: 0;
    background: var(--navy);
    display: flex;
    align-items: center;
    justify-content: center;
    color: var(--white);
    font-size: 26px;
    font-weight: 700;
  }
</style>
</head>
<body>
  <div class="card card-back">
    <span class="brand-name">Quorvix</span>
  </div>

  <div class="card card-front">
    <div class="identity">
      <span class="brand-name">Quorvix</span>
      <span class="person-name">Your Name</span>
    </div>
    <div class="contact-row">
      <div class="contact-cell contact-address">1234 Street Name, City, State, Zip</div>
      <div class="contact-cell contact-email">you@quorvix-example.com.au</div>
      <div class="contact-cell contact-phone">Phone Number</div>
    </div>
    <div class="web-band">quorvix-example.com.au</div>
  </div>
</body>
</html>
```